lumVex mobile app needs Banner Ad

"See who is around"
I'm looking for a Banner Ad for mobile application. The application is available at Fernway Shelf and Quillon Depot. Details are on the website:
http://lumvex.example

Video is here:
http://vidnook.example/Qr8Tz2Wm4Lp

I'd either use the mobile app button or the globe from logo in Banner Ad.

Sizes needed are:
320x50
640x100

```html
<!DOCTYPE html>
<html lang="en">
<head>
<meta charset="utf-8">
<title>lumVex – Banner Ads</title>
<link href="https://fonts.googleapis.com/css2?family=Source+Sans+3:wght@600;700&display=swap" rel="stylesheet">
<style>
  :root {
    --canvas: #141414;
    --blue-deep: #0f5fae;
    --blue-mid: #1d7fd0;
    --blue-light: #5aaee0;
    --map-tone: #e6e0cc;
    --map-water: #a9cde6;
    --phone-body: #1c1c1c;
    --brown-dark: #6e3512;
    --brown: #a0541f;
    --brown-light: #c27336;
    --star: #f4a62a;
    --white: #ffffff;
  }
  * { box-sizing: border-box; margin: 0; padding: 0; }
  html, body {
    width: 1200px; height: 401px; overflow: hidden;
    background: var(--canvas);
    font-family: "Source Sans 3", "Myriad Pro", sans-serif;
  }
  .stage { position: relative; width: 1200px; height: 401px; }

  .banner {
    position: absolute;
    width: 1145px; height: 175px;
    overflow: hidden;
    background: linear-gradient(90deg, var(--blue-deep) 0%, var(--blue-mid) 45%, var(--blue-light) 62%, #b9d7e4 70%, var(--map-tone) 78%);
    transform-origin: 0 0;
  }
  .banner--large { left: 55px; top: 168px; }
  .banner--small { left: 603px; top: 46px; transform: scale(0.5214); }

  .brand {
    position: absolute; left: 22px; top: 17px;
    width: 137px; height: 137px;
    display: flex; flex-direction: column; align-items: center; justify-content: center; gap: 8px;
  }
  .brand__mark {
    width: 96px; height: 96px; border-radius: 20px;
    background: linear-gradient(160deg, var(--brown-light), var(--brown-dark));
  }
  .brand__name { color: var(--white); font-weight: 700; font-size: 24px; line-height: 1; }

  .headline {
    position: absolute; left: 182px; top: 22px;
    color: var(--white); font-weight: 700; font-size: 58px; line-height: 56px;
    letter-spacing: -0.5px;
    text-shadow: 0 2px 3px rgba(0,0,0,0.45);
  }
  .rating { position: absolute; left: 506px; top: 94px; display: flex; gap: 4px; }
  .rating svg { width: 36px; height: 36px; }

  .phone-shot {
    position: absolute; left: 755px; top: 0; width: 148px; height: 175px;
    border-radius: 20px 20px 0 0;
    background: var(--phone-body);
    padding: 34px 8px 0;
  }
  .phone-shot__screen {
    width: 100%; height: 100%;
    background: linear-gradient(170deg, var(--map-tone) 0%, var(--map-water) 60%, var(--map-tone) 100%);
  }
  .map-area {
    position: absolute; left: 905px; top: 0; width: 240px; height: 175px;
    background: linear-gradient(135deg, #efe9d6, var(--map-tone) 60%, #d9d3bd);
  }

  .download {
    position: absolute; left: 900px; top: 50px; width: 176px; height: 66px;
    border-radius: 12px;
    background: linear-gradient(180deg, var(--brown-light), var(--brown) 55%, var(--brown-dark));
    box-shadow: 0 3px 6px rgba(0,0,0,0.45);
    color: var(--white); font-weight: 700; font-size: 21px;
    display: flex; align-items: center; justify-content: center;
  }
  .download__pointer { position: absolute; left: 976px; top: 114px; width: 24px; height: 26px; }
</style>
</head>
<body>
<div class="stage">

  <section class="banner banner--small" aria-label="lumVex banner 320 by 50">
    <div class="brand"><div class="brand__mark"></div><span class="brand__name">lumVex</span></div>
    <h2 class="headline">Everyone wants<br>to be found</h2>
    <div class="rating" aria-label="Five stars">
      <svg viewBox="0 0 24 24"><polygon fill="var(--star)" points="12,1 15,9 23,9 16.5,14 19,22 12,17 5,22 7.5,14 1,9 9,9"/></svg>
      <svg viewBox="0 0 24 24"><polygon fill="var(--star)" points="12,1 15,9 23,9 16.5,14 19,22 12,17 5,22 7.5,14 1,9 9,9"/></svg>
      <svg viewBox="0 0 24 24"><polygon fill="var(--star)" points="12,1 15,9 23,9 16.5,14 19,22 12,17 5,22 7.5,14 1,9 9,9"/></svg>
      <svg viewBox="0 0 24 24"><polygon fill="var(--star)" points="12,1 15,9 23,9 16.5,14 19,22 12,17 5,22 7.5,14 1,9 9,9"/></svg>
      <svg viewBox="0 0 24 24"><polygon fill="var(--star)" points="12,1 15,9 23,9 16.5,14 19,22 12,17 5,22 7.5,14 1,9 9,9"/></svg>
    </div>
    <div class="phone-shot"><div class="phone-shot__screen" role="img" aria-label="App screen showing a map with friend location pins"></div></div>
    <div class="map-area" role="img" aria-label="Street map of a bay-side city area"></div>
    <div class="download">Download NOW</div>
    <svg class="download__pointer" viewBox="0 0 24 26"><polygon points="0,0 24,0 12,26" fill="var(--brown-dark)"/></svg>
  </section>

  <section class="banner banner--large" aria-label="lumVex banner 640 by 100">
    <div class="brand"><div class="brand__mark"></div><span class="brand__name">lumVex</span></div>
    <h2 class="headline">Everyone wants<br>to be found</h2>
    <div class="rating" aria-label="Five stars">
      <svg viewBox="0 0 24 24"><polygon fill="var(--star)" points="12,1 15,9 23,9 16.5,14 19,22 12,17 5,22 7.5,14 1,9 9,9"/></svg>
      <svg viewBox="0 0 24 24"><polygon fill="var(--star)" points="12,1 15,9 23,9 16.5,14 19,22 12,17 5,22 7.5,14 1,9 9,9"/></svg>
      <svg viewBox="0 0 24 24"><polygon fill="var(--star)" points="12,1 15,9 23,9 16.5,14 19,22 12,17 5,22 7.5,14 1,9 9,9"/></svg>
      <svg viewBox="0 0 24 24"><polygon fill="var(--star)" points="12,1 15,9 23,9 16.5,14 19,22 12,17 5,22 7.5,14 1,9 9,9"/></svg>
      <svg viewBox="0 0 24 24"><polygon fill="var(--star)" points="12,1 15,9 23,9 16.5,14 19,22 12,17 5,22 7.5,14 1,9 9,9"/></svg>
    </div>
    <div class="phone-shot"><div class="phone-shot__screen" role="img" aria-label="App screen showing a map with friend location pins"></div></div>
    <div class="map-area" role="img" aria-label="Street map of a bay-side city area"></div>
    <div class="download">Download NOW</div>
    <svg class="download__pointer" viewBox="0 0 24 26"><polygon points="0,0 24,0 12,26" fill="var(--brown-dark)"/></svg>
  </section>

</div>
</body>
</html>
```